Let's help people Orlanta with better hearing!

I need a business card for my private practice. I am a Dr. of Audiology and focus on hearing and tinnitus (ringing in the ears) treatment. My practice is named "Orlanta Hearing and Tinnitus Solutions". I want to communicate the idea of improved quality of life utilizing a natural color pallet Love the color turquoise as an accent. Want a professional look, while eye catching. I'm open to nontraditional design aesthetic. Something to get excited about and motivate people to improve their lives!

```html
<!DOCTYPE html>
<html lang="en">
<head>
<meta charset="utf-8">
<title>Orlanta Hearing and Tinnitus Solutions — Business Card</title>
<link rel="stylesheet" href="https://fonts.googleapis.com/css2?family=Exo+2:wght@300;400&family=Oswald:wght@600&display=swap">
<style>
  :root {
    --backdrop: #e4e5e7;
    --card: #ffffff;
    --ink: #1e1e1e;
    --band-dark: #262626;
    --band-grey: #8e8e8e;
    --accent: #19a6e0;
    --light-text: #ffffff;
    --muted: #4a4a4a;
  }
  * { box-sizing: border-box; margin: 0; padding: 0; }
  html, body { width: 1200px; height: 902px; overflow: hidden; }
  body {
    background: var(--backdrop);
    font-family: "Exo 2", sans-serif;
    color: var(--ink);
    position: relative;
  }
  .card {
    position: absolute;
    top: 136px;
    width: 360px;
    height: 630px;
    background: var(--card);
    box-shadow: 0 10px 30px rgba(0,0,0,0.18);
    overflow: hidden;
  }
  .card--front { left: 210px; }
  .card--back { left: 630px; }

  .brand {
    position: absolute;
    left: 0; right: 0;
    text-align: center;
    font-family: "Exo 2", sans-serif;
    font-weight: 300;
    color: var(--ink);
  }
  .card--front .brand { top: 150px; }
  .card--back .brand { top: 270px; }
  .brand__name { display: block; font-size: 48px; letter-spacing: 1px; line-height: 1; }
  .brand__tagline { display: block; font-size: 12px; letter-spacing: 2px; text-transform: uppercase; margin-top: 10px; }

  .person {
    position: absolute;
    top: 318px;
    left: 40px;
  }
  .person__name {
    font-family: "Oswald", sans-serif;
    font-weight: 600;
    font-size: 28px;
    letter-spacing: 0.5px;
    text-transform: uppercase;
    line-height: 1.1;
  }
  .person__role {
    font-size: 15px;
    letter-spacing: 2.5px;
    text-transform: uppercase;
    color: var(--muted);
  }

  .band { position: absolute; left: 0; right: 0; }
  .band--contact {
    top: 398px;
    height: 86px;
    background: var(--band-dark);
    display: grid;
    grid-template-columns: 1fr 1.35fr;
    align-content: center;
    row-gap: 12px;
    padding: 0 18px 0 40px;
  }
  .band--address {
    top: 484px;
    height: 86px;
    background: var(--band-grey);
    display: flex;
    align-items: center;
    gap: 14px;
    padding-left: 40px;
  }

  .contact {
    display: flex;
    align-items: center;
    gap: 7px;
    color: var(--light-text);
    font-size: 11.5px;
    white-space: nowrap;
  }
  .contact__icon {
    width: 16px; height: 16px;
    background: var(--light-text);
    border-radius: 3px;
    display: flex; align-items: center; justify-content: center;
    flex-shrink: 0;
  }

  .address__icon {
    width: 30px; height: 30px;
    background: var(--accent);
    border-radius: 4px;
    display: flex; align-items: center; justify-content: center;
    flex-shrink: 0;
  }
  .address__text {
    color: var(--light-text);
    font-size: 15px;
    letter-spacing: 1px;
    line-height: 1.35;
  }
</style>
</head>
<body>

  <section class="card card--front" aria-label="Business card front">
    <div class="brand">
      <span class="brand__name">Orlanta</span>
      <span class="brand__tagline">Hearing &amp; Tinnitus Solutions</span>
    </div>

    <div class="person">
      <p class="person__name">Dana Whitfield</p>
      <p class="person__role">General Manager</p>
    </div>

    <div class="band band--contact">
      <div class="contact">
        <span class="contact__icon">
          <svg width="10" height="10" viewBox="0 0 10 10"><path d="M2 1 L3.6 1 L4.2 3 L3.2 3.8 Q4 5.6 6.2 6.8 L7 5.8 L9 6.4 L9 8 Q9 9 8 9 Q1 8.4 1 2 Q1 1 2 1Z" fill="#262626"/></svg>
        </span>
        012 555 0147
      </div>
      <div class="contact">
        <span class="contact__icon">
          <svg width="10" height="10" viewBox="0 0 10 10"><rect x="1" y="2.2" width="8" height="5.6" rx="0.6" fill="#262626"/><path d="M1.4 2.6 L5 5.4 L8.6 2.6" fill="none" stroke="#fff" stroke-width="0.8"/></svg>
        </span>
        hello@orlantahearing.com
      </div>
      <div class="contact">
        <span class="contact__icon">
          <svg width="10" height="10" viewBox="0 0 10 10"><rect x="2.6" y="0.6" width="4.8" height="8.8" rx="0.8" fill="#262626"/><rect x="3.4" y="1.6" width="3.2" height="5.6" fill="#fff"/></svg>
        </span>
        012 555 0147
      </div>
      <div class="contact">
        <span class="contact__icon">
          <svg width="10" height="10" viewBox="0 0 10 10"><circle cx="5" cy="5" r="4" fill="none" stroke="#262626" stroke-width="1"/><ellipse cx="5" cy="5" rx="1.8" ry="4" fill="none" stroke="#262626" stroke-width="0.8"/><line x1="1" y1="5" x2="9" y2="5" stroke="#262626" stroke-width="0.8"/></svg>
        </span>
        www.orlantahearing.com
      </div>
    </div>

    <div class="band band--address">
      <span class="address__icon">
        <svg width="16" height="18" viewBox="0 0 16 18"><path d="M8 1 C4.1 1 1.5 3.8 1.5 7.2 C1.5 11.5 8 17 8 17 C8 17 14.5 11.5 14.5 7.2 C14.5 3.8 11.9 1 8 1Z" fill="#fff"/><circle cx="8" cy="7" r="2.4" fill="#19a6e0"/></svg>
      </span>
      <p class="address__text">42 Meadow Lane,<br>Suite 3 Riverside</p>
    </div>
  </section>

  <section class="card card--back" aria-label="Business card back">
    <div class="brand">
      <span class="brand__name">Orlanta</span>
      <span class="brand__tagline">Hearing &amp; Tinnitus Solutions</span>
    </div>
  </section>

</body>
</html>
```